Flyer Design for Promoting Arborist Business

Hi guys,
***UPDATE: File pack is available here: https://www.filecrate-share.net/sh/q7x2kd91mvz4ab/BXR5tnwPqLeZsHuYdJ0c_b?dl=0
We've are a high-end arborist business in Edinburgh and we're now looking to create some promotional flyers to attract new business.
This is an open brief and we're looking for inspiration from our designer.
Our target market for the flyers is people who cannot readily access our online material (e.g. elderly people without internet access), so therefore has to be easily understood.
Trust is a central part of our business and we'd like our photographs on the flyer to build that trust.
The primary method of contact will be telephone, therefore we'd like our phone numbers to be front and centre.
You can see our website here: www.moravelmtreecare.com
We have a full pack of design material for our logo which can be shared. This includes colours, fonts and logo. It's all as per our website.
Inspire us!
Best,
Lewis

```html
<!DOCTYPE html>
<html lang="en">
<head>
<meta charset="UTF-8">
<title>Moravel Tree Care – Flyer</title>
<link href="https://fonts.googleapis.com/css2?family=Ubuntu:wght@400;500;700&family=Open+Sans:wght@700;800&display=swap" rel="stylesheet">
<style>
  :root {
    --brand-red: #b5191f;
    --deep-red: #9e1418;
    --ink: #2b2b2b;
    --paper: #ffffff;
    --backdrop: #f1f1f1;
    --bark-dark: #4a3d33;
    --bark-mid: #8a7867;
    --leaf: #6f8f3a;
  }
  html, body {
    margin: 0;
    width: 1200px;
    height: 1200px;
    overflow: hidden;
    background: var(--backdrop);
  }
  .flyer-stage {
    position: absolute;
    left: 212px;
    top: 50px;
    width: 990px;
    height: 1402px;
    transform: scale(0.785);
    transform-origin: 0 0;
  }
  .flyer {
    position: relative;
    width: 990px;
    height: 1402px;
    background: var(--paper);
    box-shadow: 0 6px 30px rgba(0,0,0,0.25);
    overflow: hidden;
    font-family: "Ubuntu", sans-serif;
    color: var(--ink);
  }
  .hero-shape {
    position: absolute;
    left: 0; top: 0;
  }
  .brand-name {
    position: absolute;
    top: 150px;
    left: 0;
    width: 990px;
    text-align: center;
    font-family: "Ubuntu", sans-serif;
    font-weight: 400;
    font-size: 46px;
    letter-spacing: 3px;
    color: #ffffff;
    margin: 0;
  }
  .headline {
    position: absolute;
    left: 0;
    width: 990px;
    text-align: center;
    margin: 0;
    font-family: "Open Sans", sans-serif;
    font-weight: 800;
    line-height: 1;
  }
  .headline-top {
    top: 250px;
    font-size: 44px;
    color: #ffffff;
    text-shadow: 0 2px 6px rgba(0,0,0,0.5);
  }
  .headline-main {
    top: 305px;
    font-size: 72px;
    color: var(--brand-red);
  }
  .team-portrait {
    position: absolute;
    border-radius: 50%;
    border: 4px solid var(--brand-red);
    box-shadow: 0 0 0 3px #ffffff;
    background: radial-gradient(circle at 50% 40%, #d98d6a 0%, #c0563c 35%, #6d8b45 70%, #3f5a2a 100%);
  }
  .portrait-one   { left: 78px;  top: 420px; width: 190px; height: 190px; }
  .portrait-two   { left: 383px; top: 493px; width: 218px; height: 218px; background: radial-gradient(circle at 50% 40%, #cfa08a 0%, #d0643f 38%, #f4f4f4 75%, #dddddd 100%); }
  .portrait-three { left: 725px; top: 457px; width: 218px; height: 218px; }

  .section-title {
    position: absolute;
    margin: 0;
    font-weight: 500;
    color: var(--brand-red);
    line-height: 1;
  }
  .services-title { left: 30px; top: 684px; font-size: 50px; }
  .qualifications-title { left: 548px; top: 754px; font-size: 38px; font-weight: 700; }

  .service-list {
    position: absolute;
    top: 742px;
    list-style: none;
    margin: 0;
    padding: 0;
  }
  .service-list li {
    height: 56px;
    font-size: 23px;
    font-weight: 500;
    display: flex;
    align-items: center;
    white-space: nowrap;
  }
  .service-list .tick {
    width: 30px;
    height: 26px;
    margin-right: 2px;
    flex: none;
  }
  .service-col-one { left: 25px; }
  .service-col-two { left: 292px; top: 744px; }

  .qualifications-text {
    position: absolute;
    left: 548px;
    top: 798px;
    width: 410px;
    font-size: 18.5px;
    line-height: 24px;
    color: #3a3a3a;
  }
  .qualifications-text p { margin: 0 0 24px; }

  .planning-note {
    position: absolute;
    left: 31px;
    top: 1150px;
    width: 480px;
    margin: 0;
    font-size: 21.5px;
    line-height: 28px;
  }
  .climber-scene {
    position: absolute;
    right: 0;
    top: 1080px;
    width: 520px;
    height: 210px;
    background: linear-gradient(160deg, rgba(255,255,255,0) 20%, rgba(150,150,150,0.35) 65%, rgba(80,80,80,0.55) 100%);
  }
  .partner-badge {
    position: absolute;
    top: 1210px;
    height: 76px;
    border-radius: 6px;
  }
  .badge-one { left: 568px; width: 62px; background: #8fa25b; border-radius: 4px; }
  .badge-two { left: 640px; width: 98px; background: #ffffff; border: 3px solid var(--brand-red); }

  .call-bar {
    position: absolute;
    left: 0;
    bottom: 0;
    width: 990px;
    height: 113px;
    background: var(--brand-red);
    display: flex;
    align-items: center;
    justify-content: center;
  }
  .call-bar p {
    margin: 0;
    color: #ffffff;
    font-family: "Open Sans", sans-serif;
    font-weight: 700;
    font-size: 60px;
    letter-spacing: 0.5px;
  }
</style>
</head>
<body>
<div class="flyer-stage">
  <div class="flyer">
    <svg class="hero-shape" width="990" height="640" viewBox="0 0 990 640">
      <defs>
        <linearGradient id="heroTones" x1="0" y1="0" x2="1" y2="1">
          <stop offset="0" stop-color="#7a2a26"/>
          <stop offset="0.35" stop-color="#5e4a3c"/>
          <stop offset="0.7" stop-color="#8a7867"/>
          <stop offset="1" stop-color="#a99a88"/>
        </linearGradient>
      </defs>
      <path role="img" aria-label="Photo of an arborist in helmet and harness climbing and cutting a large tree trunk"
            d="M0 0 H990 V460 C820 560 600 600 440 560 C280 520 120 470 0 425 Z" fill="url(#heroTones)"/>
      <path d="M0 425 C120 470 280 520 440 560 C600 600 820 560 990 460" fill="none" stroke="#b5191f" stroke-width="5"/>
    </svg>

    <p class="brand-name">MORAVEL TREE CARE</p>
    <h1 class="headline headline-top">PROFESSIONAL EDINBURGH-BASED</h1>
    <h2 class="headline headline-main">TREE SURGEONS</h2>

    <div class="team-portrait portrait-one" role="img" aria-label="Portrait of a smiling team member wearing a red helmet"></div>
    <div class="team-portrait portrait-two" role="img" aria-label="Portrait of a team member wearing an orange helmet and safety glasses"></div>
    <div class="team-portrait portrait-three" role="img" aria-label="Portrait of a smiling team member wearing an orange helmet with ear defenders"></div>

    <h3 class="section-title services-title">Our Service</h3>

    <svg width="0" height="0" style="position:absolute">
      <symbol id="tick" viewBox="0 0 30 26">
        <path d="M2 15 L10 23 L28 3 L11 17 Z" fill="#b5191f"/>
      </symbol>
    </svg>

    <ul class="service-list service-col-one">
      <li><svg class="tick"><use href="#tick"/></svg>Aerial Pruning</li>
      <li><svg class="tick"><use href="#tick"/></svg>Aerial Dismantling</li>
      <li><svg class="tick"><use href="#tick"/></svg>Clear Felling</li>
      <li><svg class="tick"><use href="#tick"/></svg>Crown Lifts</li>
      <li><svg class="tick"><use href="#tick"/></svg>Crown Reductions</li>
      <li><svg class="tick"><use href="#tick"/></svg>Emergency Response</li>
      <li><svg class="tick"><use href="#tick"/></svg>Garden Clearance</li>
    </ul>
    <ul class="service-list service-col-two">
      <li><svg class="tick"><use href="#tick"/></svg>Sectional Felling</li>
      <li><svg class="tick"><use href="#tick"/></svg>Site Clearance</li>
      <li><svg class="tick"><use href="#tick"/></svg>Storm Damage</li>
      <li><svg class="tick"><use href="#tick"/></svg>Stump Removal</li>
      <li><svg class="tick"><use href="#tick"/></svg>Tree Surveys</li>
      <li><svg class="tick"><use href="#tick"/></svg>Waste Removal</li>
      <li><svg class="tick"><use href="#tick"/></svg>Wood Chipping</li>
    </ul>

    <div class="climber-scene" role="img" aria-label="Faded silhouette of a climber working in a bare tree"></div>

    <h3 class="section-title qualifications-title">Our Qualifications</h3>
    <div class="qualifications-text">
      <p>We're fully qualified and certified by both Arbor Skills Board and Grovecert in aerial and ground-based tree work.</p>
      <p>Our arborist team is trained in the latest arborist techniques and furnished with state-of-the-art equipment to ensure that your tree work is carried out to the highest standard, quickly and with maximum safety.</p>
      <p>We can quickly reduce tree cuttings on site and we provide our disposal services as standard on every job.</p>
    </div>

    <p class="planning-note">We offer a free planning application service to manage the necessary permissions for trees with Tree Protection Orders (TPOs) and in Conservation Areas.</p>

    <div class="partner-badge badge-one" role="img" aria-label="Qualification badge"></div>
    <div class="partner-badge badge-two" role="img" aria-label="Training award badge"></div>

    <div class="call-bar">
      <p>Call Us : 0131 496 0732</p>
    </div>
  </div>
</div>
</body>
</html>
```